Wool Product Label / Yarn Band

Looking to update the packaging on our wool products. This includes a design for a paper band to place around braided wool or yarn, and a design for a sticker to place on the outside of tissue paper wrapping. Open to updating or modifying the logo, which does not fit well on a round sticker, but the sticker could also be something wool related (like a sheep or drop spindle) that does not include the logo.
Target Market(s)
Wool crafters (knitters / spinners / felters). Mainly women, aged 30-70
Industry/Entity Type
Textile
Colors
Designer to choose colors to be used in the design.
Requirements
Must have
- Band needs to include, brand name, logo, url (fernloomery.net), dyelot number, as well as the fiber content (ex: Merino Wool) and weight of the fiber (ex: 4oz).
Nice to have
- Band would ideally be easily customized because the weight and fiber content is variable and will be printed specifically for each product, Variable information can be on a sticker or printed directly on a band that can be printed on a standard printer. Attached is a photo of the current band and it's application.

```html
<!DOCTYPE html>
<html lang="en">
<head>
<meta charset="utf-8">
<title>Fernloomery — Yarn Band &amp; Sticker</title>
<link rel="stylesheet" href="https://fonts.googleapis.com/css2?family=Roboto+Condensed:wght@400;500&family=Manrope:wght@500;600;700&display=swap">
<style>
  :root {
    --page: #ffffff;
    --brand-green: #7cbc45;
    --tagline-grey: #6a6a6a;
    --ink: #4f4f4f;
    --lavender: #ddd0e3;
    --sky: #acd8e4;
    --purple: #8858a6;
    --white: #ffffff;
    --serial-grey: #8a8a8a;
  }
  * { margin: 0; padding: 0; box-sizing: border-box; }
  html, body { width: 1200px; height: 960px; overflow: hidden; background: var(--page); }
  body { position: relative; font-family: "Manrope", sans-serif; }

  /* ---------- Yarn band ---------- */
  .yarn-band {
    position: absolute; left: 226px; top: 169px; width: 750px; height: 240px;
    box-shadow: 6px 8px 8px rgba(0,0,0,0.28);
    overflow: hidden;
  }
  .band-artwork {
    position: absolute; left: 0; top: 0; width: 750px; height: 146px;
    background: linear-gradient(90deg,
      #eeeaf1 0%, #f6e3dc 14%, #f7e6cc 26%, #f8ecd4 40%, #e3edf5 46%,
      #e6f1f4 62%, #f7e6df 70%, #f6e2dc 80%, #e3f3ee 86%, #f7e3df 94%, #f8e6e1 100%);
  }
  .band-brand {
    position: absolute; left: 0; right: 0; top: 40px; text-align: center;
  }
  .brand-name {
    font-family: "Roboto Condensed", sans-serif; font-weight: 500;
    font-size: 45px; line-height: 1; color: var(--brand-green); letter-spacing: -0.5px;
  }
  .band-tagline {
    position: absolute; left: 318px; top: 94px;
    font-family: "Roboto Condensed", sans-serif; font-weight: 500;
    font-size: 15px; color: var(--tagline-grey);
  }
  .serial-number {
    position: absolute; left: 12px; top: 200px; transform-origin: 0 0; transform: rotate(-90deg);
    font-family: "Manrope", sans-serif; font-size: 9px; font-weight: 500;
    color: var(--serial-grey); white-space: nowrap; letter-spacing: 0.2px;
  }
  .band-fiber {
    position: absolute; left: 0; top: 146px; width: 424px; height: 58px;
    background: var(--lavender);
    display: flex; align-items: center; justify-content: flex-end; padding-right: 8px;
    font-size: 16px; font-weight: 600; color: var(--ink);
  }
  .band-weight {
    position: absolute; left: 424px; top: 146px; width: 326px; height: 58px;
    background: var(--sky);
    display: flex; align-items: center; padding-left: 10px;
    font-size: 18px; font-weight: 600; color: var(--ink);
  }
  .band-url {
    position: absolute; left: 0; top: 204px; width: 750px; height: 36px;
    background: var(--purple); color: var(--white);
    display: flex; align-items: center; justify-content: center;
    font-size: 15.5px; font-weight: 700;
  }
  .serial-number { z-index: 2; }

  /* ---------- Round sticker ---------- */
  .round-sticker { position: absolute; left: 420px; top: 482px; width: 370px; height: 370px; }
  .sticker-brand { font-family: "Roboto Condensed", sans-serif; font-weight: 500; fill: var(--brand-green); }
  .sticker-tagline { font-family: "Roboto Condensed", sans-serif; font-weight: 500; fill: var(--tagline-grey); }
  .sticker-info { font-family: "Manrope", sans-serif; font-weight: 600; fill: var(--ink); }
  .sticker-url { font-family: "Manrope", sans-serif; font-weight: 700; fill: var(--white); letter-spacing: 0.4px; }
</style>
</head>
<body>

  <section class="yarn-band" aria-label="Yarn band">
    <div class="band-artwork" role="img" aria-label="Faint photo of hand painted yarn skeins in pastel colours"></div>
    <div class="band-brand"><span class="brand-name">fernloomery</span></div>
    <div class="band-tagline">hand painted yarn &amp; fibers</div>
    <div class="band-fiber">85% Merino Wool / 15% Silk</div>
    <div class="band-weight">Qty: 4.0 oz</div>
    <div class="band-url">www.fernloomery.net</div>
    <div class="serial-number">S/N: MER/SILK-BLEND1</div>
  </section>

  <svg class="round-sticker" viewBox="0 0 370 370" aria-label="Round sticker">
    <defs>
      <clipPath id="sticker-inner"><circle cx="180" cy="180" r="134"/></clipPath>
      <linearGradient id="sticker-yarn" x1="0" y1="0" x2="1" y2="0">
        <stop offset="0" stop-color="#ecebf3"/>
        <stop offset="0.25" stop-color="#f5ddd4"/>
        <stop offset="0.5" stop-color="#f8ebcf"/>
        <stop offset="0.8" stop-color="#f7e8d8"/>
        <stop offset="1" stop-color="#deecf3"/>
      </linearGradient>
      <path id="url-arc" d="M 24 180 A 156 156 0 0 0 336 180"/>
    </defs>

    <circle cx="186" cy="187" r="165" fill="rgba(0,0,0,0.35)"/>
    <circle cx="180" cy="180" r="165" fill="var(--purple)"/>
    <circle cx="180" cy="180" r="138" fill="var(--sky)"/>

    <g clip-path="url(#sticker-inner)">
      <rect x="40" y="40" width="280" height="192" fill="url(#sticker-yarn)" role="img" aria-label="Faint photo of hand painted yarn skeins"/>
      <rect x="40" y="232" width="280" height="43" fill="var(--lavender)"/>
      <rect x="40" y="275" width="280" height="60" fill="var(--sky)"/>
    </g>

    <text class="sticker-brand" x="180" y="160" font-size="36" text-anchor="middle">fernloomery</text>
    <text class="sticker-tagline" x="202" y="185" font-size="13" text-anchor="middle">hand painted yarn &amp; fibers</text>
    <text class="sticker-info" x="178" y="259" font-size="15" text-anchor="middle">85% Merino Wool / 15% Silk</text>
    <text class="sticker-info" x="180" y="300" font-size="16" text-anchor="middle">Qty: 4.0 oz</text>

    <text class="sticker-url" font-size="15">
      <textPath href="#url-arc" startOffset="50%" text-anchor="middle">www.fernloomery.net</textPath>
    </text>
  </svg>

</body>
</html>
```